Letterhead Design for Vostrand Corporate Stationery

We are seeking a talented designer on ArtHive to create a professional and cohesive corporate stationery set for our company, Vostrand. Vostrand is a prominent player in the Commercial Real Estate industry, and we need stationery that reflects our brand's excellence and professionalism.

Scope of Work:

1. Letterhead Template (Microsoft Word):

Design a letterhead template in Microsoft Word format that adheres to our brand standards (attached in project files).
Include all necessary elements such as company logo, address, contact information, and any other relevant details.
The letterhead should be clean, elegant, and suitable for official business correspondence.

2. Business Cards:

Design business cards for our team members using the provided brand guidelines.
Include name, title, contact information, and the Vostrand logo.
Create a design that leaves a lasting impression and reflects our brand's professionalism.

3. Envelopes:

Design envelopes in various sizes (e.g., standard letter and legal sizes) that match the overall stationery theme.
Ensure that the design includes our company name, logo, and return address in accordance with brand guidelines.

4. Stationery:

Create a visually appealing stationery template that can be used for various documents and correspondence.
Ensure that the stationery design aligns with our brand standards and maintains consistency across all materials.

Submission Requirements:

Provide high-resolution files for each item (letterhead, business cards, envelopes, and stationery) in formats suitable for both print and digital use.
Include editable source files (e.g., Adobe Illustrator, Photoshop) for future modifications if necessary.

Design Guidelines:

Our brand is known for professionalism, trustworthiness, and excellence in the Commercial Real Estate industry. Please adhere to the brand standards provided in the project attachments.
Use our company colors, fonts, and logo as specified in the brand guidelines.
Feel free to be creative within the boundaries of our brand to make our stationery stand out while maintaining a professional look.

Budget and Timeline:

We are looking for high-quality designs at a competitive price.
The project timeline is flexible, but we would appreciate prompt responses from designers.
Please submit your best pricing and estimated delivery times with your proposals.
We look forward to receiving your creative and professional designs that will represent Vostrand in the best possible light. Thank you for considering our project, and we can't wait to see your submissions on ArtHive!

Target Market(s)

Our primary target market for the corporate stationery design project includes, but is not limited to: Investors: Individuals or entities interested in commercial real estate investment opportunities. Brokers: Commercial real estate brokers who facilitate property transactions and negotiations. Tenant Representatives: Professionals who advocate for the interests of tenants in commercial lease transactions. Lenders: Financial institutions and lenders involved in providing financing for commercial real estate projects. Property Owners: Owners of commercial real estate properties seeking professional correspondence materials. Industry Partners: Professionals and organizations within the commercial real estate industry who collaborate with or provide services to Vostrand. Prospective Clients: Potential clients or partners exploring opportunities in the commercial real estate sector. Please note that while these are the primary target market segments, the stationery design should also appeal to a broader audience within the commercial real estate industry and convey professionalism and trustworthiness to all stakeholders.

Industry/Entity Type

Commercial Real Estate

Font styles to use
Sans Serif

Colors
0054AA
0677BA
7BADD7
CADEEF
E8F1F8
0094D4
00A9DD
6FCCEA
C7EBF8
E9F6FB
F0912C
F2A743
F7CA91
FBE8D2
FDF5EE
EE7325
F08F49
F5BC92
FAE3D3
FDF4ED

Requirements
Must have
• Brand Consistency: Ensure that the design adheres to Vostrand's existing brand standards and guidelines (provided in project attachments). Professional Appearance: The stationery must convey professionalism, trustworthiness, and excellence in the Commercial Real Estate industry. Logo Usage: Integrate the Vostrand logo prominently and appropriately on all stationery items. Contact Information: Include accurate contact details, such as the company's address, phone number, email address, and website URL. Typography: Use the specified fonts from the brand guidelines for all text elements, maintaining consistency in font style and size. Color Palette: Utilize the designated brand colors consistently throughout the design. File Formats: Ensure that the final design files are provided in high-resolution formats suitable for both print and digital use. Also, request editable source files (e.g., Adobe Illustrator, Photoshop) for future modifications if needed. Print-Ready: Prepare the design files to be print-ready, including the appropriate bleed and margin specifications for printing purposes. Stationery Variations: Include designs for letterhead, business cards, envelopes (multiple sizes if applicable), and general stationery. Creativity within Brand Guidelines: Encourage designers to be creative while working within the boundaries of Vostrand's brand standards, making the stationery unique and eye-catching. Versatility: Ensure that the stationery can be easily adapted for various purposes, such as formal business correspondence, presentations, and more. Timely Delivery: Specify your preferred timeline for receiving initial design concepts and revisions. Budget: Indicate your budget range for the project to attract designers who can provide high-quality work within your financial constraints. Responsive Designers: Request that designers are responsive to messages and able to make necessary revisions in a timely manner.
Nice to have
• Creative Elements: Incorporate unique and creative design elements that align with Vostrand's brand identity and the Commercial Real Estate industry. Texture or Embossing: If applicable and within budget, consider incorporating textured or embossed elements to add a tactile dimension to the stationery. Custom Illustrations: Include custom illustrations or graphics that convey the essence of the commercial real estate industry or your company's mission and values. Watermark or Background Pattern: Consider adding a subtle watermark or background pattern that complements the overall design without distracting from the content. Custom Typography: Explore the use of custom typography or stylized lettering for headers or key text elements to make the stationery more visually appealing. Enhanced Print Options: If budget allows, opt for premium printing techniques like foil stamping, spot UV, or letterpress to make the stationery truly stand out. Digital Templates: Request digital templates for electronic documents, such as Microsoft Word templates, PowerPoint templates, or PDF templates, to maintain consistency in digital communications. Multiple Design Concepts: Ask for variations of the stationery design to choose from, providing you with options for different occasions or purposes. QR Codes: If relevant, consider incorporating QR codes that link to Vostrand's website, portfolio, or contact information for convenient access. Environmentally Friendly Options: Explore eco-friendly printing materials and practices to align with sustainability goals, if applicable. Mobile Optimization: Ensure that any digital templates or elements are optimized for mobile use, enhancing accessibility and usability. Social Media Icons: Include social media icons and links to Vostrand's social media profiles, if desired, for a comprehensive online presence. Alternate Color Schemes: Request variations of the design with alternate color schemes for seasonal or special occasions.
Should not have
• Non-Compliance with Brand Guidelines: Specify that the design must strictly adhere to Vostrand's brand guidelines, and any deviations are not acceptable. Excessive Complexity: Avoid overly complex designs that may clutter the stationery or distract from the essential information. Inconsistent Branding: Ensure that all design elements, including colors, fonts, and logo usage, remain consistent with the provided brand standards. Unapproved Fonts: Specify that designers should only use the approved fonts from the brand guidelines and avoid introducing new fonts. Inappropriate Imagery: Request that designers refrain from using images, illustrations, or graphics that are unrelated to the Commercial Real Estate industry or that could potentially be perceived as unprofessional. Overly Bright Colors: If it doesn't align with your brand, discourage the use of overly bright or neon colors that may not convey professionalism. Clashing Color Schemes: Ensure that the color scheme chosen for the design is harmonious and avoids color combinations that clash or are difficult to read. Overuse of Effects: Discourage excessive use of visual effects, such as gradients, drop shadows, or excessive transparency, which can make the stationery appear cluttered. Extravagant Printing Costs: Specify that designers should consider budget constraints and avoid design elements that would significantly increase printing costs, unless the budget allows for premium printing techniques. Outdated Design Trends: Request that the design avoids incorporating outdated design trends that may make the stationery appear dated. Inconsistent Branding Across Items: Ensure that the design maintains consistency across all stationery items (letterhead, business cards, envelopes, etc.) and that there are no significant variations that could create confusion. Overly Busy Layouts: Ask for designs that have a clean and professional appearance, avoiding overcrowded layouts that make it difficult to read or find essential information.

```html
<!DOCTYPE html>
<html lang="en">
<head>
<meta charset="utf-8">
<title>Vostrand Stationery</title>
<link href="https://fonts.googleapis.com/css2?family=Montserrat:wght@400;500;600&family=Source+Sans+3:wght@400;600&display=swap" rel="stylesheet">
<style>
  :root {
    --backdrop: #a9a8aa;
    --paper: #f1f0f1;
    --navy: #0b1d4b;
    --brand-blue: #3b72b9;
    --ink: #3a3a3c;
    --muted: #6b6b70;
    --on-navy: #ffffff;
  }
  * { margin: 0; padding: 0; box-sizing: border-box; }
  html, body { width: 1200px; height: 770px; overflow: hidden; }
  body {
    background: var(--backdrop);
    position: relative;
    font-family: "Source Sans 3", sans-serif;
    color: var(--ink);
  }
  .item { position: absolute; background: var(--paper); overflow: hidden; }
  .wordmark {
    font-family: "Montserrat", sans-serif;
    font-weight: 600;
    color: var(--navy);
    letter-spacing: 0.14em;
    white-space: nowrap;
  }
  .band { position: absolute; left: 0; bottom: 0; width: 100%; display: block; }
  .band-url {
    position: absolute; bottom: 0; right: 0;
    font-family: "Montserrat", sans-serif;
    color: var(--on-navy);
  }

  /* Business card, dark front */
  .card-front { left: 86px; top: 46px; width: 218px; height: 125px; background: var(--navy); }
  .card-front .wordmark {
    position: absolute; left: 0; right: 0; top: 52px; text-align: center;
    font-size: 13px; color: var(--on-navy);
  }
  .card-front .card-url {
    position: absolute; left: 0; right: 0; top: 107px; text-align: center;
    font-family: "Montserrat", sans-serif; font-size: 5.5px; letter-spacing: 0.08em; color: var(--on-navy);
  }

  /* Business card, contact back */
  .card-back { left: 337px; top: 46px; width: 218px; height: 125px; }
  .card-back .wordmark { position: absolute; left: 14px; top: 57px; font-size: 10px; }
  .card-back .divider { position: absolute; left: 113px; top: 29px; width: 1px; height: 66px; background: #c9c9cc; }
  .card-back .contact { position: absolute; left: 123px; top: 31px; font-family: "Montserrat", sans-serif; line-height: 1.25; }
  .card-back .person { font-size: 7px; font-weight: 600; color: var(--navy); }
  .card-back .role { font-size: 4.6px; color: var(--muted); margin-bottom: 6px; }
  .card-back .line { font-size: 4.6px; color: var(--muted); display: flex; align-items: center; gap: 3px; }
  .card-back .address { margin-bottom: 5px; }
  .card-back .band-url { font-size: 5px; right: 6px; line-height: 10px; }

  /* Envelope, front */
  .envelope-front { left: 61px; top: 203px; width: 560px; height: 254px; }
  .envelope-front .wordmark { position: absolute; left: 30px; top: 54px; font-size: 14px; }
  .envelope-front .return-address { position: absolute; left: 30px; top: 106px; font-size: 7.6px; line-height: 1.3; }
  .envelope-front .band-url { font-size: 7.5px; right: 30px; line-height: 19px; }

  /* Envelope, back with flap */
  .envelope-back { left: 57px; top: 479px; width: 560px; height: 254px; }
  .envelope-back .flap { position: absolute; left: 0; top: 0; width: 560px; height: 94px; display: block; }
  .envelope-back .wordmark {
    position: absolute; left: 0; right: 0; top: 40px; text-align: center;
    font-size: 11px; color: var(--on-navy);
  }

  /* Letterhead */
  .letterhead { left: 643px; top: 33px; width: 496px; height: 701px; }
  .letterhead .wordmark { position: absolute; left: 45px; top: 62px; font-size: 14px; }
  .letterhead .sender {
    position: absolute; left: 367px; top: 39px; font-size: 7.6px; line-height: 1.28; color: var(--ink);
  }
  .letterhead .sender .line { display: flex; align-items: center; gap: 5px; color: var(--muted); }
  .letterhead .sender .address { margin-bottom: 4px; }
  .letterhead .date { position: absolute; left: 48px; top: 177px; font-size: 9px; font-weight: 600; }
  .letterhead .recipient { position: absolute; left: 48px; top: 212px; font-size: 9px; font-weight: 600; line-height: 1.34; }
  .letterhead .body { position: absolute; left: 47px; top: 282px; width: 402px; font-size: 7.7px; line-height: 12px; text-align: justify; }
  .letterhead .body p { margin-bottom: 12px; }
  .letterhead .signature-mark {
    position: absolute; left: 358px; top: 528px; width: 80px; height: 30px;
    background: linear-gradient(90deg, rgba(30,30,40,0.12), rgba(30,30,40,0.05));
  }
  .letterhead .signer { position: absolute; left: 377px; top: 557px; font-size: 7.8px; color: var(--ink); }
  .letterhead .band-url { font-size: 7.5px; right: 35px; line-height: 19px; }
</style>
</head>
<body>

  <section class="item card-front" aria-label="Business card front">
    <div class="wordmark">VOSTRAND</div>
    <div class="card-url">www.vostrand.com</div>
  </section>

  <section class="item card-back" aria-label="Business card back">
    <div class="wordmark">VOSTRAND</div>
    <div class="divider"></div>
    <div class="contact">
      <div class="person">ELENA MARSH</div>
      <div class="role">Managing Director</div>
      <div class="address">
        <div class="line">214 Harbor Crest Road</div>
        <div class="line">Halden Bay, 55120</div>
      </div>
      <div class="line">
        <svg width="4" height="4" viewBox="0 0 10 10"><path d="M2 1 L4 1 L5 3.5 L3.7 4.5 Q4.8 6.4 5.5 6.3 L6.5 5 L9 6 L9 8 Q5 9.5 1 2 Z" fill="#0b1d4b"/></svg>555-210-4418
      </div>
      <div class="line">
        <svg width="4" height="4" viewBox="0 0 10 10"><rect x="2.5" y="0.5" width="5" height="9" rx="1" fill="none" stroke="#0b1d4b" stroke-width="1.4"/></svg>555-210-4419
      </div>
      <div class="line">
        <svg width="4" height="4" viewBox="0 0 10 10"><rect x="0.5" y="2" width="9" height="6" fill="#0b1d4b"/><path d="M0.5 2 L5 5.5 L9.5 2" stroke="#fff" stroke-width="0.9" fill="none"/></svg>info@vostrand.com
      </div>
    </div>
    <svg class="band" width="218" height="10" viewBox="0 0 218 10">
      <polygon points="0,0 153,0 150,4 0,4" fill="#3b72b9"/>
      <polygon points="0,6 149,6 154,0 218,0 218,10 0,10" fill="#0b1d4b"/>
    </svg>
    <div class="band-url">www.vostrand.com</div>
  </section>

  <section class="item envelope-front" aria-label="Envelope front">
    <div class="wordmark">VOSTRAND</div>
    <div class="return-address">214 Harbor Crest Road<br>Halden Bay, 55120</div>
    <svg class="band" width="560" height="19" viewBox="0 0 560 19">
      <polygon points="0,0 436,0 431,7 0,7" fill="#3b72b9"/>
      <polygon points="0,10 430,10 438,0 560,0 560,19 0,19" fill="#0b1d4b"/>
    </svg>
    <div class="band-url">www.vostrand.com</div>
  </section>

  <section class="item envelope-back" aria-label="Envelope back">
    <svg class="flap" width="560" height="94" viewBox="0 0 560 94">
      <path d="M0 0 H560 L546 64 Q540 94 510 94 H50 Q20 94 14 64 Z" fill="#0b1d4b"/>
    </svg>
    <div class="wordmark">VOSTRAND</div>
  </section>

  <section class="item letterhead" aria-label="Letterhead">
    <div class="wordmark">VOSTRAND</div>
    <div class="sender">
      <div class="address">214 Harbor Crest Road<br>Halden Bay, 55120</div>
      <div class="line"><svg width="7" height="7" viewBox="0 0 10 10"><path d="M2 1 L4 1 L5 3.5 L3.7 4.5 Q4.8 6.4 5.5 6.3 L6.5 5 L9 6 L9 8 Q5 9.5 1 2 Z" fill="#0b1d4b"/></svg>555-210-4418</div>
      <div class="line"><svg width="7" height="7" viewBox="0 0 10 10"><rect x="2.5" y="0.5" width="5" height="3" fill="#0b1d4b"/><rect x="0.5" y="4" width="9" height="4" fill="#0b1d4b"/><rect x="2.5" y="7" width="5" height="2.5" fill="#0b1d4b"/></svg>555-210-4419</div>
      <div class="line"><svg width="7" height="7" viewBox="0 0 10 10"><rect x="0.5" y="2" width="9" height="6" fill="#0b1d4b"/><path d="M0.5 2 L5 5.5 L9.5 2" stroke="#fff" stroke-width="0.9" fill="none"/></svg>info@vostrand.com</div>
    </div>

    <div class="date">Port Alden, October 12, 2015</div>
    <div class="recipient">Sr.<br>TOMAS RIVEL<br>Web Master<br>City</div>

    <div class="body">
      <p>Contrary to popular belief, Lorem Ipsum is not simply random text. It has roots in a piece of classical Latin literature from 45 BC, making it over 2000 years old. Martin Ellory, a Latin professor at Halbrook College, looked up one of the more obscure Latin words, consectetur, from a Lorem Ipsum passage, and going through the cites of the word in classical literature,</p>
      <p>discovered the undoubtable source. Lorem Ipsum comes from sections 1.10.32 and 1.10.33 of "de Finibus Bonorum et Malorum" (The Extremes of Good and Evil) by Tertius Marcell, written in 45 BC. This book is a treatise on the theory of ethics, very popular during the Renaissance. The first line of Lorem Ipsum, "Lorem ipsum dolor sit amet..", comes from a line in section 1.10.32.</p>
      <p>The standard chunk of Lorem Ipsum used since the 1500s is reproduced below for those interested. Sections 1.10.32 and 1.10.33 from "de Finibus Bonorum et Malorum" by Tertius Marcell are also reproduced in their exact original form, accompanied by English versions from the 1914 translation by E. Whitlow.</p>
      <p>There are many variations of passages of Lorem Ipsum available, but the majority have suffered alteration in some form, by injected humour, or randomised words which don't look even slightly believable. If you are going to use a passage of Lorem Ipsum, you need to be sure there isn't anything embarrassing hidden in the middle of text. All the Lorem Ipsum generators o</p>
    </div>

    <div class="signature-mark" role="img" aria-label="Handwritten signature of Adrian Kell"></div>
    <div class="signer">CEO/ FOUNDER</div>

    <svg class="band" width="496" height="19" viewBox="0 0 496 19">
      <polygon points="0,0 368,0 363,6 0,6" fill="#3b72b9"/>
      <polygon points="0,9 361,9 369,0 496,0 496,19 0,19" fill="#0b1d4b"/>
    </svg>
    <div class="band-url">www.vostrand.com</div>
  </section>

</body>
</html>
```